Brand Business Card for Hotel Cloud Management System

Hello designers,
we are looking for a new brand business card for our product Stayvora. Our brand Stayvora is a hotel management system for small hotels, B&B, guesthouses etc. and just recently we are expanding our offer to other European markets. Therefore we need a business card that will communicate not only to the end-users (hoteliers) but also to potential business partners/ We would like the brand business card to be professional looking, but not too serius, modern, elegant, clean, Our brand color is orange, dark grey and it would be nice to see both combined.

Please visit our website www.stayvora.eu to get more impression on what our brand stayvora stands for.

Please find attached stayvora logo.

Target Market(s)

small hotels, hoteliers, B&B owners, potential business partners

Industry/Entity Type

Software Service

Contact Information for Business Card

Stayvora
- hotel software solutions - web booking engine - multi channel manager
www.stayvora.eu
T: +38614738265
E: info@stayvora.net

Font styles to use
Serif
Sans Serif

Colors
f37122
aaaaaa
606060
f6f6f6

Requirements
Must have
• Logo of the brand
• the layout of the business card should be in connection with the look and feel of the website stayvora.eu and logo stayvora;

```html
<!DOCTYPE html>
<html lang="en">
<head>
<meta charset="utf-8">
<title>Stayvora – Business Card</title>
<link rel="stylesheet" href="https://fonts.googleapis.com/css2?family=Nunito:wght@800&family=Quicksand:wght@500&display=swap">
<style>
  :root {
    --brand-orange: #f37122;
    --brand-orange-deep: #e8641a;
    --brand-dark: #1f1f1f;
    --text-grey: #3a3a3a;
    --paper: #ffffff;
    --backdrop: #e6e6e6;
  }
  html, body {
    margin: 0;
    width: 1200px;
    height: 1200px;
    overflow: hidden;
    background: var(--backdrop);
  }
  .stage {
    width: 1200px;
    height: 1200px;
    display: flex;
    align-items: center;
    justify-content: center;
  }
  .business-card {
    width: 1000px;
    height: 620px;
    filter: drop-shadow(0 10px 24px rgba(0,0,0,0.18));
  }
  .card-paper { fill: var(--paper); }
  .brand-name {
    font-family: "Nunito", sans-serif;
    font-weight: 800;
    font-size: 92px;
    fill: var(--brand-dark);
    letter-spacing: -2px;
  }
  .brand-dot { fill: var(--brand-orange); }
  .brand-tagline {
    font-family: "Quicksand", sans-serif;
    font-weight: 500;
    font-size: 26px;
    fill: var(--brand-dark);
  }
  .contact-line {
    font-family: "Quicksand", sans-serif;
    font-weight: 500;
    font-size: 30px;
    fill: var(--text-grey);
  }
  .contact-icon-bg { fill: var(--brand-orange); }
  .contact-icon-line { fill: none; stroke: #fff; stroke-width: 1.6; stroke-linecap: round; stroke-linejoin: round; }
  .contact-icon-fill { fill: #fff; }
</style>
</head>
<body>
<main class="stage">
  <svg class="business-card" viewBox="0 0 1000 620" xmlns="http://www.w3.org/2000/svg" aria-label="Stayvora business card">
    <defs>
      <clipPath id="card-shape">
        <rect x="0" y="0" width="1000" height="620" rx="38" ry="38"/>
      </clipPath>
      <linearGradient id="wave-fill" x1="0" y1="0" x2="1" y2="1">
        <stop offset="0" stop-color="var(--brand-orange)"/>
        <stop offset="1" stop-color="var(--brand-orange-deep)"/>
      </linearGradient>
    </defs>

    <g clip-path="url(#card-shape)">
      <rect class="card-paper" x="0" y="0" width="1000" height="620"/>

      <g class="brand-wave" role="img" aria-label="Orange wave panels with a repeating pattern of service keywords">
        <path fill="url(#wave-fill)" d="M 640 0 L 880 0 C 830 18, 790 40, 770 78 C 748 118, 710 138, 640 132 Z"/>
        <path fill="url(#wave-fill)" d="M 565 620 L 565 400 C 565 310, 595 262, 660 255 C 740 248, 830 232, 905 192 C 950 170, 980 160, 1000 156 L 1000 620 Z"/>
      </g>

      <g class="brand-block">
        <text class="brand-name" x="72" y="220">Stayvora</text>
        <circle class="brand-dot" cx="538" cy="150" r="14"/>
        <text class="brand-tagline" x="82" y="262">hotel pms service</text>
      </g>

      <g class="contact-list">
        <g class="contact-item">
          <circle class="contact-icon-bg" cx="96" cy="470" r="13"/>
          <circle class="contact-icon-line" cx="96" cy="470" r="7"/>
          <path class="contact-icon-line" d="M89 470 H103 M96 463 C92 467 92 473 96 477 M96 463 C100 467 100 473 96 477"/>
          <text class="contact-line" x="122" y="480">www.stayvora.eu</text>
        </g>
        <g class="contact-item">
          <circle class="contact-icon-bg" cx="96" cy="514" r="13"/>
          <path class="contact-icon-fill" d="M91 507 l3 -1 l2 4 l-2 2 c1 2 3 4 5 5 l2 -2 l4 2 l-1 3 c-7 1 -14 -6 -13 -13 z"/>
          <text class="contact-line" x="122" y="524">+38614738265</text>
        </g>
        <g class="contact-item">
          <circle class="contact-icon-bg" cx="96" cy="558" r="13"/>
          <rect class="contact-icon-line" x="89" y="553" width="14" height="10" rx="1"/>
          <path class="contact-icon-line" d="M89 553 L96 559 L103 553"/>
          <text class="contact-line" x="122" y="568">info@stayvora.net</text>
        </g>
      </g>
    </g>
  </svg>
</main>
</body>
</html>
```